Packing Design: SNACK FOOD BAG

We are manufactures and our main product is a kind of shell-shaped corn puff in ketchup flavor: brand name is Zebrin. (See photo Red Zebrin Flips Ketchup)

We will launch 15 new products (like chips, tortilla, popcorn, biscuits, etc.) under the same logo Zebrin.
As new Products are different, their layout must be different or with different designs.
But they must all be connected together with any feature, to be easily recognized / identified as same Zebrin range of products.
-

THE MAIN PURPOSE OF THIS PROJECT CONTEST IS:

Choosing the best connection between “Red Zebrin flips ketchup" label and new designs for new products.
Customers must easily understand that new products are done from same Zebrin Factory and are part of the same Zebrin brand (production). We want new labels to naturally derive from old Zebrin design with a modern and hip connection.

We would prefer drafts where 1 part is in red color (including Zebrin Logo) and the rest of layout to be used for different designs (for different products). At the end of all different designs, they may have in common a part of their layouts, derived from Red Zebrin Ketchup.
But we warmly welcome your different ideas and different suggestions.

-
Send sample draft for any from products below:
PEANUT BUTTER CORN bag size: High 210 mm x Width 145 mm
TORTILLA CHIPS ( flavors: Nachos / Spicy Ketchup) bag size: High 160 mm x Width 130 mm
CRUNCHY CROUTONS bag size: High 160 mm x Width 115 mm
CARAMEL CORN bag size: High 210 mm x Width 145 mm

Bags are (no transparent) BOPP material, with different sizes, containing small quantities from 20 – 50 grams.
-
Details for this project can be downloaded clicking to the link below:
http://www.filevault-example.net/file/4r8k21 and
http://www.filevault-example.net/file/w73m5q

Reason: there are designers submitting designs at the last moments. there is no time to review and give feedback to all. apologies for any inconvenience caused to the designers who submitted earlier warm regards

Target Market(s)

Target customers are young people: children, teens, students.

Industry/Entity Type

Factory

Requirements
Must have
• The new designs must include SAME Zebrin Logo, few pieces of the product view with flavor images and FEATURES CONNECTING ALL DESIGNS TOGETHER.
Nice to have
• A Feature is needed, to connect all new products with "Zebrin flips ketchup" design and all designs together.
Connections could be any details like:
RED COLORED ribbons, RED COLORED dotted /spotted layout,
RED COLORED background containing lines within itself,
different nuances of Zebrin Logo,
or else, or else, etc.
Show us what inspires you...

We would like to see strong deep colors, with 3D or fading reflections within them.
Final designs should bring the sense of appetite (making your mouth wet).
Should not have
• - Zebrin-Logo must be used without the word 'Flips"
- Must no have connection with ZEBRIN carton character.
- we don't like that all products to be in all-in-red bags.

```html
<!DOCTYPE html>
<html lang="en">
<head>
<meta charset="utf-8">
<title>Zebrin Snack Range</title>
<link href="https://fonts.googleapis.com/css2?family=Roboto+Condensed:wght@400;700;900&family=Kalam:wght@700&display=swap" rel="stylesheet">
<style>
  :root{
    --stage-light:#f4f4f4;
    --stage-dark:#c9c9c9;
    --bag-white:#ffffff;
    --ink:#111111;
    --maker-green:#2f9a3a;
    --corn-1:#f7d24a; --corn-2:#e9a31c;
    --nacho-ribbon-1:#f7c23b; --nacho-ribbon-2:#e49a1a; --nacho-text:#6b3f0c;
    --ketchup-1:#d9262b; --ketchup-2:#8e0d12;
    --ketchup-ribbon:#161616;
    --choc-1:#8a5634; --choc-2:#4f2a17;
    --choc-ribbon-1:#9b2d1d; --choc-ribbon-2:#5e1a10;
    --caramel-1:#f7b045; --caramel-2:#e0761a;
    --caramel-ribbon-1:#f08a2a; --caramel-ribbon-2:#d45c12;
    --pb-1:#e2bb84; --pb-2:#b98a52;
    --pb-ribbon-1:#cf2f35; --pb-ribbon-2:#941a20;
    --chip-1:#f6c54c; --chip-2:#d98b1f;
    --puff-choc-1:#a8693f; --puff-choc-2:#6b3a1e;
    --puff-car-1:#ffd36a; --puff-car-2:#eb9a2b;
    --puff-pb-1:#f9d27a; --puff-pb-2:#e6a443;
  }
  *{box-sizing:border-box;margin:0;padding:0}
  html,body{width:1200px;height:900px;overflow:hidden}
  body{
    position:relative;
    background:radial-gradient(ellipse at 50% 40%,var(--stage-light) 0%,#e3e3e3 60%,var(--stage-dark) 100%);
    font-family:"Roboto Condensed",Arial,sans-serif;
  }
  .bag{
    position:absolute;
    background:var(--bag-white);
    border-radius:8px;
    overflow:hidden;
    box-shadow:0 14px 22px rgba(0,0,0,.18);
  }
  .bag--small{width:275px;height:305px}
  .bag--large{width:345px;height:440px}

  .bag__art{position:absolute;left:0;top:0;width:100%}
  .bag--small .bag__art{height:165px}
  .bag--large .bag__art{height:215px}

  .bag__maker{
    position:absolute;top:10px;left:12px;
    font-weight:700;font-size:13px;color:var(--maker-green);
  }
  .bag__brand{
    position:absolute;left:0;width:100%;text-align:center;
    font-weight:900;color:var(--ink);letter-spacing:-1px;line-height:1;
  }
  .bag--small .bag__brand{top:36px;font-size:58px}
  .bag--large .bag__brand{top:68px;font-size:78px}

  .bag__ribbon{
    position:absolute;left:0;width:100%;
    text-align:center;color:#fff;
    clip-path:polygon(0 14%,100% 0,100% 86%,0 100%);
    display:flex;flex-direction:column;justify-content:center;line-height:1;
  }
  .bag--small .bag__ribbon{top:112px;height:62px}
  .bag--large .bag__ribbon{top:168px;height:86px}
  .bag__flavor{font-weight:700;text-transform:uppercase}
  .bag--small .bag__flavor{font-size:26px}
  .bag--large .bag__flavor{font-size:36px}
  .bag__kind{font-size:14px;margin-top:2px}
  .bag--large .bag__kind{font-size:18px}

  .bag__tagline{
    position:absolute;left:0;width:100%;text-align:center;
    font-family:"Kalam",cursive;color:var(--ink);
  }
  .bag--small .bag__tagline{top:176px;font-size:16px}
  .bag--large .bag__tagline{top:258px;font-size:22px}

  .bag__product{position:absolute;left:50%;transform:translateX(-50%);border-radius:46% 54% 40% 50%}
  .bag--small .bag__product{top:196px;width:170px;height:92px}
  .bag--large .bag__product{top:296px;width:230px;height:120px}

  /* flavours */
  .nachos .bag__art{background:linear-gradient(160deg,var(--corn-1),var(--corn-2))}
  .nachos .bag__ribbon{background:linear-gradient(180deg,var(--nacho-ribbon-1),var(--nacho-ribbon-2));color:var(--nacho-text)}
  .spicy-ketchup .bag__art{background:radial-gradient(circle at 50% 40%,var(--ketchup-1),var(--ketchup-2))}
  .spicy-ketchup .bag__ribbon{background:var(--ketchup-ribbon)}
  .tortilla .bag__product{background:radial-gradient(circle at 45% 40%,var(--chip-1),var(--chip-2))}

  .chocolate .bag__art{background:radial-gradient(circle at 60% 25%,var(--choc-1),var(--choc-2))}
  .chocolate .bag__ribbon{background:linear-gradient(180deg,var(--choc-ribbon-1),var(--choc-ribbon-2))}
  .chocolate .bag__product{background:radial-gradient(circle at 45% 40%,var(--puff-choc-1),var(--puff-choc-2))}

  .caramel .bag__art{background:linear-gradient(170deg,var(--caramel-1),var(--caramel-2))}
  .caramel .bag__ribbon{background:linear-gradient(180deg,var(--caramel-ribbon-1),var(--caramel-ribbon-2))}
  .caramel .bag__product{background:radial-gradient(circle at 45% 40%,var(--puff-car-1),var(--puff-car-2))}

  .peanut-butter .bag__art{background:radial-gradient(circle at 50% 40%,var(--pb-1),var(--pb-2))}
  .peanut-butter .bag__ribbon{background:linear-gradient(180deg,var(--pb-ribbon-1),var(--pb-ribbon-2))}
  .peanut-butter .bag__product{background:radial-gradient(circle at 45% 40%,var(--puff-pb-1),var(--puff-pb-2))}
</style>
</head>
<body>

<section class="bag bag--small tortilla nachos" style="left:275px;top:55px">
  <div class="bag__art" role="img" aria-label="Close-up of a golden corn cob"></div>
  <div class="bag__maker">Crunvale</div>
  <div class="bag__brand">Zebrin</div>
  <div class="bag__ribbon"><span class="bag__flavor">Nachos</span><span class="bag__kind">Tortilla chips</span></div>
  <div class="bag__tagline">greate taste!</div>
  <div class="bag__product" role="img" aria-label="Pile of seasoned tortilla chips"></div>
</section>

<section class="bag bag--small tortilla spicy-ketchup" style="left:635px;top:55px">
  <div class="bag__art" role="img" aria-label="Swirl of red ketchup"></div>
  <div class="bag__maker">Crunvale</div>
  <div class="bag__brand">Zebrin</div>
  <div class="bag__ribbon"><span class="bag__flavor">Spicy Ketchup</span><span class="bag__kind">Tortilla chips</span></div>
  <div class="bag__tagline">greate taste!</div>
  <div class="bag__product" role="img" aria-label="Pile of tortilla chips with ketchup"></div>
</section>

<section class="bag bag--large chocolate" style="left:62px;top:350px">
  <div class="bag__art" role="img" aria-label="Swirl of melted chocolate"></div>
  <div class="bag__maker">Crunvale</div>
  <div class="bag__brand">Zebrin</div>
  <div class="bag__ribbon"><span class="bag__flavor">Chocolate</span><span class="bag__kind">Corn</span></div>
  <div class="bag__tagline">greate taste!</div>
  <div class="bag__product" role="img" aria-label="Chocolate coated corn puffs"></div>
</section>

<section class="bag bag--large caramel" style="left:430px;top:385px">
  <div class="bag__art" role="img" aria-label="Flowing golden caramel"></div>
  <div class="bag__maker">Crunvale</div>
  <div class="bag__brand">Zebrin</div>
  <div class="bag__ribbon"><span class="bag__flavor">Caramel</span><span class="bag__kind">Corn</span></div>
  <div class="bag__tagline">greate taste!</div>
  <div class="bag__product" role="img" aria-label="Caramel coated corn puffs"></div>
</section>

<section class="bag bag--large peanut-butter" style="left:795px;top:372px">
  <div class="bag__art" role="img" aria-label="Spread of peanut butter on toast"></div>
  <div class="bag__maker">Crunvale</div>
  <div class="bag__brand">Zebrin</div>
  <div class="bag__ribbon"><span class="bag__flavor">Peanut Butter</span><span class="bag__kind">Corn</span></div>
  <div class="bag__tagline">greate taste!</div>
  <div class="bag__product" role="img" aria-label="Peanut butter corn puff curls"></div>
</section>

</body>
</html>
```